Edgy book cover - contemporary fiction

A book cover design for a first-time author. The book is being self-published, but needs to stand out as a quality product amongst a huge number of self-published titles hitting the market.

About the book
“Moths Above the Stairwell” is a collection of eleven fictional short stories, set in the the turbulent economic times of The Great Recession (Or the Global Financial Crisis). The stories are about ordinary people and their struggles and hopes, as they cope with the circumstances that are dealt them: losing their jobs and homes, helping friends in trouble, making their own success, having to move across town or across the world to survive, having to go back to work after losing their retirement savings.

The book is being published as an e-book only at this stage. The graphic will be viewed as an icon on the zentora plumet store (and similar stores such as Orvex vellumo), and as a larger image on the book's own page. In future, the cover may be used in a print version.

I expect to be challenged and stimulated along the way as I don’t have a firm view of what the final cover will look like – it really is up to you to wow me. I value your time and as such I will commit to giving each designer feedback.

Required Deliverables

Although you need only submit the book cover at the design stage the required project deliverables are:
- Book Front Cover - colour. Main focus
- Other versions once finalised:
- Colour image image 928px wide by 1250px high, at 150ppi,
- B&W image 96ppi B/W, and it will resize automatically to 600px by 800px, which is perfect for the inside Plumet cover.
- 6 by 4 inch postcards and A4 posters for promotional purposes
- Final tag-line applied to all of the above
- Front, back and spine book cover design for future printing of physical book, size 5.25 inches by 8 inches. Zentora Marvonix template available when number of pages has been finalised.
- At least 2 iterations of the winning design

Target Market(s)

The target for this book is a broad, educated middle-class audience, say over age 30, for whom home, mortgage and job are real concerns.

Industry/Entity Type

Printing

Requirements
Must have
• The cover needs to be edgy but not overdone. Less is more in this case. Think about the target audience and their tastes. I think the title gives lots of creative possibility, so please be creative and clever. I’d like people to look at the cover and think “Cool/Clever cover – I’d better read this”. Be original yet keep the end product accessible.

There will be a tag-line on the cover somewhere. Where you locate it is up to you, but you need to leave space for it. For the time being please use the text “Notes from Uneasy Seasons ” – but this may change by the end of the project.

The following text of title, tagline and author

Moths Above the Stairwell
Notes from Uneasy Seasons
Neil Pashby

Purely as guidance to my taste, some book covers I like are:

http://lnkvo.net/qa4rt
http://lnkvo.net/8k3pw
http://lnkvo.net/mebxo
http://lnkvo.net/r7tnc
http://lnkvo.net/4ujd2
http://lnkvo.net/hqefz
Should not have
• Please avoid clichés and being “overly busy”. Although the book is to be self published on a low budget it shouldn’t look like that. If the cover would look right on a popular mass fiction title then it is probably not right for me.

The design should not use a cliched "happy families" house image.

It needs not to look like it's based on a book cover template from a self-publishing house.

Some examples of book covers I don’t like are :

http://lnkvo.net/9pgk1
http://lnkvo.net/5xraw
http://lnkvo.net/c62yb
http://lnkvo.net/jlu84
http://lnkvo.net/f0smv

```html
<!DOCTYPE html>
<html lang="en">
<head>
<meta charset="utf-8">
<title>Moths Above the Stairwell — Neil Pashby</title>
<link rel="stylesheet" href="https://fonts.googleapis.com/css2?family=Raleway:wght@200;300&display=swap">
<style>
  :root {
    --paper: #ffffff;
    --frame: #9a9a9a;
    --ink: #1a1a1a;
    --ink-soft: #6e6e6e;
    --roof-grey: #8d8f93;
    --roof-light: #c9c7c4;
    --roof-red: #a4463a;
  }
  html, body {
    margin: 0;
    padding: 0;
    width: 878px;
    height: 1200px;
    overflow: hidden;
    background: var(--paper);
  }
  .cover {
    position: relative;
    width: 878px;
    height: 1200px;
    background: var(--paper);
    font-family: "Raleway", "Helvetica Neue", Arial, sans-serif;
  }
  .cover-frame {
    position: absolute;
    left: 50px;
    top: 30px;
    width: 785px;
    height: 1136px;
    border: 1.5px solid var(--frame);
    box-sizing: border-box;
  }
  .author {
    position: absolute;
    left: 94px;
    top: 48px;
    margin: 0;
    font-weight: 300;
    font-size: 62px;
    letter-spacing: 4px;
    color: var(--ink-soft);
    line-height: 1;
  }
  .title {
    position: absolute;
    left: 92px;
    top: 142px;
    margin: 0;
    font-weight: 200;
    font-size: 86px;
    line-height: 0.98;
    letter-spacing: 1px;
    color: var(--ink);
    text-transform: uppercase;
  }
  .title span { display: block; }
  .tagline {
    position: absolute;
    left: 100px;
    top: 430px;
    margin: 0;
    font-weight: 300;
    font-size: 40px;
    color: var(--ink-soft);
    line-height: 1;
  }
  .rooftop-crack {
    position: absolute;
    left: 0;
    top: 0;
    width: 878px;
    height: 1200px;
  }
</style>
</head>
<body>
  <main class="cover">
    <div class="cover-frame"></div>
    <p class="author">Neil Pashby</p>
    <h1 class="title"><span>Moths Above</span><span>the Stairwell</span></h1>
    <p class="tagline">Notes from Uneasy Seasons</p>
    <svg class="rooftop-crack" viewBox="0 0 300 410" preserveAspectRatio="none" role="img" aria-label="Photograph of tiled suburban rooftops seen through a jagged crack opening in the cover">
      <defs>
        <linearGradient id="roofTones" x1="0.8" y1="0" x2="0.3" y2="1">
          <stop offset="0" stop-color="var(--roof-grey)"/>
          <stop offset="0.5" stop-color="var(--roof-light)"/>
          <stop offset="1" stop-color="var(--roof-red)"/>
        </linearGradient>
      </defs>
      <polygon fill="url(#roofTones)" points="285,160 268,170 255,178 262,190 240,200 232,215 220,222 210,240 200,250 185,262 188,275 170,290 160,305 145,318 150,330 130,345 120,360 110,372 100,385 95,398 285,398"/>
    </svg>
  </main>
</body>
</html>
```